Bref créative
RKT Stationery
B-Cards
I need double sided standard sized Business Card [3.5" x 2"]
Arial, Arial Black, Comic Sans MS, Courier New, Impact, Trebuchet MS and Verdana
Professional
Dorian Vasko
Operations Manager
P.O. BOX 817
Glenn Dale, MD 20769
dorian@rktbuilders.example
www.rktbuilders.example
Doesn't have to include all the information.
Atleast Company name, Logo, persons name and title.
Office number, cell, fax, and e-mail
Could have a calendar of the year, maybe QR codes for website, cell or e-mails of contact.
Anything else that could maybe go on the back of the card. I just don't want it to be blank.
vector logo file

```html
<!DOCTYPE html>
<html lang="en">
<head>
<meta charset="utf-8">
<title>RKT Stationery</title>
<link href="https://fonts.googleapis.com/css2?family=Arimo:wght@400;700&display=swap" rel="stylesheet">
<style>
  :root {
    --bg: #efe9e0;
    --paper: #ffffff;
    --red: #a3151f;
    --red-dark: #6e0a12;
    --green: #2f7a2c;
    --green-dark: #1f5a1d;
    --ink: #4a4a4a;
    --muted: #8a8a8a;
  }
  * { box-sizing: border-box; margin: 0; padding: 0; }
  html, body { width: 1200px; height: 446px; overflow: hidden; }
  body { background: var(--bg); font-family: "Arimo", Arial, sans-serif; color: var(--ink); position: relative; }
  .sheet { position: absolute; background: var(--paper); box-shadow: 0 2px 6px rgba(0,0,0,.18); overflow: hidden; }
  .swoosh { position: absolute; left: 0; bottom: 0; width: 100%; display: block; }
  .brand { display: flex; align-items: center; gap: 5px; font-weight: 700; color: var(--red); white-space: nowrap; }
  .brand-mark { width: 9px; height: 9px; background: var(--green); flex: none; }
  .small { font-size: 5px; line-height: 1.6; color: var(--muted); }
  .contact-list { position: absolute; list-style: none; }
  .contact-list li { display: flex; align-items: center; gap: 4px; }
  .contact-list li::before { content: ""; width: 4px; height: 4px; background: var(--red); border-radius: 50%; }

  /* business cards */
  .card-front { left: 12px; top: 149px; width: 96px; height: 52px; }
  .card-front .brand { position: absolute; left: 6px; top: 6px; font-size: 6px; gap: 3px; }
  .card-front .brand-mark { width: 6px; height: 6px; }
  .card-front .person { position: absolute; right: 6px; top: 15px; text-align: right; font-size: 3.5px; line-height: 1.4; color: var(--muted); white-space: nowrap; }
  .card-front .person strong { font-size: 4.5px; color: var(--red); display: block; }
  .card-back { left: 12px; top: 211px; width: 96px; height: 52px; }
  .card-back .brand { position: absolute; left: 50%; top: 14px; transform: translateX(-50%); font-size: 8px; }

  /* letterheads */
  .letterhead { top: 19px; width: 326px; height: 413px; }
  .letterhead.option-one { left: 137px; }
  .letterhead.option-two { left: 476px; }
  .letterhead .brand { position: absolute; font-size: 13px; }
  .option-one .brand { left: 24px; top: 28px; }
  .option-one .contact-list { left: 190px; top: 18px; }
  .option-two .brand { left: 50%; top: 28px; transform: translateX(-50%); }
  .letterhead .footer-text { position: absolute; right: 40px; bottom: 52px; text-align: right; }
  .watermark { position: absolute; left: 50%; top: 170px; transform: translateX(-50%); font-size: 34px; font-weight: 700; color: rgba(163,21,31,.07); white-space: nowrap; }

  /* envelopes */
  .envelope-back { left: 828px; top: 48px; width: 360px; height: 132px; }
  .envelope-front { left: 828px; top: 204px; width: 360px; height: 120px; }
  .envelope-front .brand { position: absolute; left: 50%; top: 48px; transform: translateX(-50%); font-size: 11px; }
  .envelope-card { left: 828px; top: 336px; width: 180px; height: 84px; }
  .envelope-card .brand { position: absolute; left: 50%; top: 18px; transform: translateX(-50%); font-size: 9px; }
  .envelope-card .footer-text { position: absolute; right: 12px; bottom: 18px; text-align: right; }
</style>
</head>
<body>

  <section class="sheet card-front">
    <div class="brand"><span class="brand-mark"></span>RKT Builders</div>
    <div class="person"><strong>Dorian Vasko</strong>Operations Manager<br>(301) 555-0192<br>dorian@rktbuilders.example</div>
    <svg class="swoosh" viewBox="0 0 96 14" preserveAspectRatio="none" height="14">
      <path d="M0 6 C30 14 60 0 96 4 L96 14 L0 14Z" fill="var(--green)"/>
      <path d="M0 9 C30 16 60 3 96 7 L96 14 L0 14Z" fill="var(--red)"/>
    </svg>
  </section>

  <section class="sheet card-back">
    <div class="brand"><span class="brand-mark"></span>RKT Builders</div>
    <svg class="swoosh" viewBox="0 0 96 16" preserveAspectRatio="none" height="16">
      <path d="M0 6 C30 16 60 0 96 4 L96 16 L0 16Z" fill="var(--green)"/>
      <path d="M0 9 C30 18 60 3 96 7 L96 16 L0 16Z" fill="var(--red)"/>
    </svg>
  </section>

  <section class="sheet letterhead option-one">
    <div class="brand"><span class="brand-mark"></span>RKT Builders</div>
    <ul class="contact-list small">
      <li>Dorian Vasko, Operations Manager</li>
      <li>P.O. BOX 817, Glenn Dale, MD 20769</li>
      <li>Office (301) 555-0192</li>
      <li>dorian@rktbuilders.example</li>
      <li>www.rktbuilders.example</li>
    </ul>
    <svg class="swoosh" viewBox="0 0 326 70" preserveAspectRatio="none" height="70">
      <path d="M0 20 C110 60 220 0 326 14 L326 70 L0 70Z" fill="var(--green)"/>
      <path d="M0 26 C110 66 220 6 326 20 L326 70 L0 70Z" fill="var(--red)"/>
      <path d="M0 50 C120 70 230 30 326 40 L326 70 L0 70Z" fill="var(--red-dark)" opacity=".5"/>
    </svg>
  </section>

  <section class="sheet letterhead option-two">
    <div class="brand"><span class="brand-mark"></span>RKT Builders</div>
    <div class="watermark">RKT Builders</div>
    <div class="footer-text small">P.O. BOX 817<br>Glenn Dale, MD 20769<br>www.rktbuilders.example</div>
    <svg class="swoosh" viewBox="0 0 326 50" preserveAspectRatio="none" height="50">
      <path d="M0 30 C120 50 230 0 326 10 L326 50 L0 50Z" fill="var(--green)"/>
      <path d="M0 34 C120 54 230 6 326 16 L326 50 L0 50Z" fill="var(--red)"/>
    </svg>
  </section>

  <section class="sheet envelope-back">
    <svg width="360" height="132" viewBox="0 0 360 132">
      <defs>
        <linearGradient id="flapRed" x1="0" y1="0" x2="0" y2="1">
          <stop offset="0" stop-color="var(--red-dark)"/>
          <stop offset="1" stop-color="var(--red)"/>
        </linearGradient>
      </defs>
      <rect width="360" height="132" fill="var(--paper)"/>
      <rect width="360" height="90" fill="url(#flapRed)"/>
      <path d="M8 30 L352 30 L352 70 L180 96 L8 70Z" fill="var(--green)"/>
      <path d="M0 132 L180 104 L360 132" fill="none" stroke="#dcdcdc" stroke-width="1"/>
    </svg>
  </section>

  <section class="sheet envelope-front">
    <div class="brand"><span class="brand-mark"></span>RKT Builders</div>
  </section>

  <section class="sheet envelope-card">
    <div class="brand"><span class="brand-mark"></span>RKT Builders</div>
    <div class="footer-text small">P.O. BOX 817<br>Glenn Dale, MD 20769</div>
  </section>

</body>
</html>
```